Educational Management System User Interface (Vantro Design Concepts)

Hi,I require a 1-page design for an educational management system. The image attached shows all required elements and also their locations. I require the design to be based on vantro-styled interfaces using elements from: http://qelvo.hostrun.io/qelvo-kitset/ & http://layoutmintly.com/layout-template/admin . Side menu's should not be too large that they hide the main content of the page.
Sorry very slight addition to the design as per new uploaded file.
I like how the elements of the vantro hub page are seperated with the background colour and white boxes. This could maybe work in the design as per the uploaded image?
Thanks,
Melvin
Reason: Some designers have some submissions.

```html
<!DOCTYPE html>
<html lang="en">
<head>
<meta charset="utf-8">
<title>Kestrel LMS – Timeline</title>
<link href="https://fonts.googleapis.com/css2?family=Roboto:ital,wght@0,400;0,500;0,700;1,400&display=swap" rel="stylesheet">
<style>
:root{
  --bg:#e5e5e5;--white:#fff;--panel:#f5f5f5;--line:#e3e3e3;
  --text:#222;--muted:#777;--soft:#999;
  --green:#3e9e2e;--green-btn:#4caf3c;--green-dark:#2f7d1e;
  --blue:#4285f4;--info:#8fb0e8;--red:#e8594e;--orange:#e8743b;--yellow:#f2b000;
}
*{box-sizing:border-box;margin:0;padding:0}
html,body{width:1200px;height:1163px;overflow:hidden}
body{background:var(--bg);font-family:"Roboto",Arial,sans-serif;color:var(--text);position:relative}
.abs{position:absolute}
/* header */
.topbar{position:absolute;left:0;top:0;width:1200px;height:41px;background:var(--white);box-shadow:0 1px 3px rgba(0,0,0,.12);z-index:2}
.brand{position:absolute;left:17px;top:12px;font-size:15px;display:flex;align-items:center;gap:6px}
.brand-dot{width:14px;height:14px;border-radius:50%;background:var(--yellow)}
.nav-icons{position:absolute;left:254px;top:11px;display:flex;gap:16px}
.user{position:absolute;right:65px;top:12px;font-size:15px}
.avatar-sm{position:absolute;right:11px;top:5px;width:31px;height:31px;border-radius:50%;background:linear-gradient(135deg,#6a7a8c,#2e3640)}
.badge{position:absolute;left:957px;top:6px;background:#d9342b;color:#fff;font-size:9px;padding:0 2px;line-height:12px}
/* left sidebar */
.sidebar{position:absolute;left:0;top:41px;width:212px;background:var(--white)}
.side-head{height:42px;display:flex;align-items:center;gap:10px;padding-left:18px;font-size:14px;color:#555;border-bottom:1px solid var(--line)}
.side-ico{width:18px;height:18px;border-radius:50%;background:var(--blue)}
.groups{padding:14px 0 20px 44px}
.groups h4{font-size:13.5px;font-weight:500;color:#666;margin-bottom:6px}
.groups li{list-style:none;font-size:13px;color:#777;line-height:21px}
.btn-green{display:block;width:126px;height:26px;margin-top:10px;background:var(--green);border:1px solid var(--green-dark);color:#fff;font-size:10.5px;font-weight:500;text-align:center;line-height:24px}
.groups .btn-green:first-of-type{margin-top:20px}
.community{border-top:1px solid var(--line);border-bottom:1px solid var(--line)}
.logout{height:41px;background:var(--panel);display:flex;align-items:center;gap:10px;padding-left:18px;font-size:14px}
/* right sidebar */
.events{position:absolute;left:960px;top:41px;width:240px;background:var(--white)}
.ev-head{height:47px;display:flex;align-items:center;padding-left:10px;gap:10px;font-size:12.5px;font-weight:500;color:#666;letter-spacing:.3px;border-bottom:1px solid var(--line);position:relative}
.ev-head::after{content:"";position:absolute;right:14px;top:21px;border:4px solid transparent;border-top-color:#888}
.cal{width:24px;height:22px;background:#eee;border-top:6px solid var(--orange)}
.ev-row{height:38.8px;display:flex;align-items:center;padding-left:10px;gap:10px;font-size:12.5px;border-bottom:1px solid var(--line)}
.ev-row:last-child{border-bottom:0}
.ev-i{width:18px;height:18px;border-radius:50%;background:var(--info);color:#fff;font-size:11px;font-style:italic;text-align:center;line-height:18px;font-family:Georgia,serif}
.ev-row b{font-weight:500}
/* timeline */
.timeline-line{position:absolute;left:284px;top:245px;width:2px;height:603px;background:var(--white)}
.avatar{position:absolute;width:64px;height:64px;border-radius:50%;border:3px solid #fff;background:linear-gradient(135deg,#c9a27a,#4a3a2e);box-shadow:0 1px 3px rgba(0,0,0,.25)}
.refresh{position:absolute;left:268px;top:228px;width:34px;height:34px;border-radius:50%;background:#fff;display:flex;align-items:center;justify-content:center;box-shadow:0 1px 2px rgba(0,0,0,.15)}
/* composer */
.composer{position:absolute;left:346px;top:69px;width:561px;height:139px;background:var(--panel);border:1px solid #ddd;box-shadow:0 1px 2px rgba(0,0,0,.1)}
.composer-input{position:absolute;left:19px;top:18px;width:524px;height:66px;background:#fff;border:1px solid #e2e2e2;padding:11px;font-size:15px;color:#444}
.composer-tools{position:absolute;right:88px;top:97px;display:flex;gap:20px;align-items:center}
.btn-submit{position:absolute;right:19px;top:94px;width:66px;height:28px;background:var(--green-btn);color:#fff;font-size:11px;font-weight:700;text-align:center;line-height:28px}
/* post cards */
.card{position:absolute;left:346px;width:561px;background:#fff;box-shadow:0 1px 2px rgba(0,0,0,.12)}
.card-body{padding:22px 19px 18px}
.author{font-size:13.5px;font-weight:500}
.stamp{font-size:11.5px;color:var(--muted);margin-top:3px}
.excerpt{font-size:11.5px;line-height:17px;margin-top:18px}
.excerpt i{display:block}
.read{font-size:11px;color:var(--soft);margin-top:6px}
.actions{display:flex;gap:8px;margin-top:15px}
.act{width:37px;height:27px;border:1px solid #ddd;display:flex;align-items:center;justify-content:center;font-size:13px;font-weight:500;color:#444;background:#fff}
.file{display:flex;margin-top:25px}
.pdf{width:56px;height:75px;background:var(--red);color:#fff;font-size:8px;font-weight:700;display:flex;align-items:flex-end;justify-content:center;padding-bottom:20px;position:relative}
.pdf::after{content:"";position:absolute;right:0;top:0;border:6px solid transparent;border-top-color:var(--bg);border-right-color:var(--bg)}
.file-box{width:464px;height:74px;background:var(--panel);border:1px solid #ccc;padding:10px 15px;font-size:11.5px}
.btn-dl{display:inline-block;margin-top:8px;background:var(--green-btn);color:#fff;font-size:11.5px;font-weight:500;padding:0 13px;line-height:27px}
.indent{padding-left:72px}
.comments{background:var(--panel);border-top:1px solid var(--line);padding:18px 19px 19px}
.comment{display:flex;gap:10px;margin-bottom:17px;font-size:12.5px;line-height:17px}
.comment .sq{width:26px;height:26px;background:var(--blue);flex:none;margin-top:2px}
.comment b{font-weight:500}
.comment span{color:var(--soft);font-size:11px}
.add{height:28px;border:1px solid #ddd;background:#fff;font-size:11px;color:var(--soft);padding:0 8px;line-height:26px}
.loading{position:absolute;left:345px;top:1088px;width:562px;height:36px;background:var(--panel);border:1px solid #ddd;display:flex;align-items:center;justify-content:center;gap:6px;font-size:11px;color:#bbb}
.spin{width:14px;height:14px;border-radius:50%;background:#bbb}
</style>
</head>
<body>

<header class="topbar">
  <div class="brand"><span class="brand-dot"></span>Kestrel LMS</div>
  <nav class="nav-icons">
    <svg width="18" height="18" viewBox="0 0 18 18"><path d="M2 9 9 3l7 6M4 8v7h10V8" fill="none" stroke="#888" stroke-width="1.6"/></svg>
    <svg width="18" height="18" viewBox="0 0 18 18"><rect x="2" y="4" width="14" height="12" fill="#eee"/><rect x="2" y="4" width="14" height="4" fill="#e8743b"/></svg>
    <svg width="18" height="18" viewBox="0 0 18 18"><circle cx="9" cy="9" r="8" fill="#e8594e"/><path d="m5 9 3 3 5-6" fill="none" stroke="#fff" stroke-width="2"/></svg>
    <svg width="20" height="18" viewBox="0 0 20 18"><path d="M1 3h7l2 2h8v11H1z" fill="#d9472b"/></svg>
  </nav>
  <svg class="abs" style="left:947px;top:12px" width="18" height="19" viewBox="0 0 18 19"><path d="M3 14V8a6 6 0 0 1 12 0v6l2 2H1z" fill="#666"/><circle cx="9" cy="17" r="2" fill="#666"/></svg>
  <span class="badge">99</span>
  <span class="abs" style="left:993px;top:12px;width:18px;height:18px;border-radius:50%;background:#43a047"></span>
  <div class="user">Tobin Ashgrove</div>
  <div class="avatar-sm" role="img" aria-label="User profile photo"></div>
</header>

<aside class="sidebar">
  <div class="side-head"><span class="side-ico"></span>TEACHERS</div>
  <div class="groups">
    <h4>My Groups</h4>
    <ul><li>Group Name One</li><li>Group Name Two</li><li>Group Name Three</li><li>Group Name Four</li></ul>
    <span class="btn-green">Create New Group</span>
    <span class="btn-green">Join New Group</span>
  </div>
  <div class="side-head community"><span class="side-ico"></span>COMMUNITY</div>
  <div class="logout">
    <svg width="18" height="18" viewBox="0 0 18 18"><path d="M5 4a7 7 0 1 0 8 0" fill="none" stroke="#d93a2b" stroke-width="2"/><path d="M9 1v8" stroke="#d93a2b" stroke-width="2"/></svg>Log out</div>
</aside>

<aside class="events">
  <div class="ev-head"><span class="cal"></span>TODAY'S EVENTS</div>
  <div class="ev-row"><span class="ev-i">i</span><b>12:15 am</b> Meeting in the canteen</div>
  <div class="ev-row"><span class="ev-i">i</span><b>12:15 am</b> Meeting in the canteen</div>
  <div class="ev-row"><span class="ev-i">i</span><b>12:15 am</b> Meeting in the canteen</div>
  <div class="ev-row"><span class="ev-i">i</span><b>12:15 am</b> Meeting in the canteen</div>
  <div class="ev-row" style="border-bottom:1px solid var(--line)"><span class="ev-i">i</span><b>12:15 am</b> Meeting in the canteen</div>
  <div class="ev-head"><span class="cal"></span>UPCOMING EVENTS</div>
  <div class="ev-row"><span class="ev-i">i</span><b>12:15 am</b> Meeting in the canteen</div>
  <div class="ev-row"><span class="ev-i">i</span><b>12:15 am</b> Meeting in the canteen</div>
  <div class="ev-row"><span class="ev-i">i</span><b>12:15 am</b> Meeting in the canteen</div>
  <div class="ev-row"><span class="ev-i">i</span><b>12:15 am</b> Meeting in the canteen</div>
  <div class="ev-row"><span class="ev-i">i</span><b>12:15 am</b> Meeting in the canteen</div>
</aside>

<div class="timeline-line"></div>
<div class="avatar" style="left:253px;top:88px" role="img" aria-label="Profile photo of the current user"></div>
<div class="refresh"><svg width="18" height="18" viewBox="0 0 18 18"><path d="M14 6a6 6 0 1 0 1 5" fill="none" stroke="#555" stroke-width="2.4"/><path d="M15 1v6H9z" fill="#555"/></svg></div>

<section class="composer">
  <div class="composer-input">Please post your update...</div>
  <div class="composer-tools">
    <svg width="16" height="18" viewBox="0 0 16 18"><path d="M1 1h9l5 5v11H1z" fill="#f3f3f3" stroke="#ddd"/></svg>
    <svg width="18" height="18" viewBox="0 0 18 18"><path d="M7 11 11 7M6 8l-3 3a3 3 0 0 0 4 4l3-3M12 10l3-3a3 3 0 0 0-4-4L8 6" fill="none" stroke="#f2a900" stroke-width="2"/></svg>
    <svg width="20" height="16" viewBox="0 0 20 16"><rect x="1" y="3" width="18" height="12" rx="2" fill="#3b82d6"/><circle cx="10" cy="9" r="4" fill="#fff"/><circle cx="10" cy="9" r="2.5" fill="#3b82d6"/></svg>
  </div>
  <span class="btn-submit">SUBMIT</span>
</section>

<article class="card" style="top:283px">
  <div class="card-body">
    <div class="author">Darla Venhoff</div>
    <div class="stamp">4:26 PM 22/12/2014</div>
    <div class="file">
      <div class="pdf">PDF</div>
      <div class="file-box"><b style="font-weight:500">Result.pdf</b> - 2.5 MB<br><span class="btn-dl">DOWNLOAD FILE</span></div>
    </div>
    <div class="indent">
      <p class="excerpt" style="margin-top:11px">Mauris sodales, arcu quis fermentum commodo. Curabitur scelerisque massa<i>Ut sit amet vestibulum risus consectetur tortor archu quis comodo vitae urna mollis!</i>Curabitur scelerisque massa eget sem luctus, sit amet vestibulum risus mauris sodales</p>
      <p class="read">Read more</p>
    </div>
    <div class="actions"><span class="act">+5</span><span class="act"><svg width="14" height="12" viewBox="0 0 14 12"><path d="M8 1l5 4-5 4V6.5C4 6.5 2 8 1 11 1 6 4 3.5 8 3.5z" fill="#444"/></svg></span></div>
  </div>
  <div class="comments">
    <div class="comment"><span class="sq"></span><div><b>Corin T.</b> <span>4:38 PM</span><br>Lorem impsum dont not by</div></div>
    <div class="comment"><span class="sq"></span><div><b>Marlo</b> <span>4:38 PM</span><br>Lorem ipsum</div></div>
    <div class="comment"><span class="sq"></span><div><b>QuietMoss</b> <span>4:38 PM</span><br>Hello! dam</div></div>
    <div class="add">Add a comment...</div>
  </div>
</article>
<div class="avatar" style="left:253px;top:299px" role="img" aria-label="Profile photo of the post author"></div>

<article class="card" style="top:800px">
  <div class="card-body">
    <div class="author">Darla Venhoff</div>
    <div class="stamp">4:26 PM 22/12/2014</div>
    <p class="excerpt">Mauris sodales, arcu quis fermentum commodo. Curabitur scelerisque massa<i>Ut sit amet vestibulum risus consectetur tortor archu quis comodo vitae urna mollis!</i>Curabitur scelerisque massa eget sem luctus, sit amet vestibulum risus mauris sodales</p>
    <p class="read">Read more</p>
    <div class="actions"><span class="act">+5</span><span class="act"><svg width="14" height="12" viewBox="0 0 14 12"><path d="M8 1l5 4-5 4V6.5C4 6.5 2 8 1 11 1 6 4 3.5 8 3.5z" fill="#444"/></svg></span></div>
  </div>
  <div class="comments"><div class="add">Add a comment...</div></div>
</article>
<div class="avatar" style="left:253px;top:816px" role="img" aria-label="Profile photo of the post author"></div>

<div class="loading"><span class="spin"></span>Loading...</div>

</body>
</html>
```